Established food business needs a new name card design

Refer to attached current name card. Would like a new professional look design with only the company name and logo without any pictures. Would like green and yellow to be included.
To include:
My name "HAKIM RUSLAN" and hand phone number "86207319".
To delete "
"Along Pinegrove Ave 3" and
"www.bu-tirah.com.sg"
To change email to:
"rvk27@tealmail.com.sg"

```html
<!DOCTYPE html>
<html lang="en">
<head>
<meta charset="utf-8">
<title>Bu-Tirah Name Card</title>
<link rel="stylesheet" href="https://fonts.googleapis.com/css2?family=Fredoka:wght@600&family=Lato:wght@400&display=swap">
<style>
  :root {
    --backdrop: #2e2e30;
    --green-light: #0b5c37;
    --green-dark: #043822;
    --gold: #e6c514;
    --gold-deep: #b89a00;
    --gold-shine: #fff27a;
    --text-light: #f2f2ee;
  }
  * { margin: 0; padding: 0; box-sizing: border-box; }
  html, body {
    width: 1200px; height: 900px; overflow: hidden;
    background: var(--backdrop);
  }
  .canvas {
    width: 1200px; height: 900px;
    display: flex; flex-direction: column; align-items: center; justify-content: center;
    gap: 44px;
  }
  .card {
    position: relative;
    width: 580px; height: 330px;
    background: radial-gradient(ellipse at 50% 40%, var(--green-light) 0%, var(--green-dark) 85%);
    overflow: hidden;
  }
  .card__band {
    position: absolute; left: 0; right: 0; bottom: 0; height: 12px;
    background: linear-gradient(90deg, var(--gold-deep) 0%, var(--gold) 30%, var(--gold-shine) 55%, var(--gold) 75%, var(--gold-deep) 100%);
  }
  /* Front */
  .brand {
    position: absolute; left: 0; right: 0; top: 126px;
    display: flex; align-items: center; justify-content: center; gap: 14px;
  }
  .brand__dot {
    width: 34px; height: 34px; border-radius: 50%;
    background: var(--gold);
  }
  .brand__name {
    font-family: "Fredoka", sans-serif; font-weight: 600;
    font-size: 42px; letter-spacing: 1px; color: var(--gold);
  }
  /* Back */
  .holder {
    position: absolute; left: 70px; top: 112px; width: 190px;
    text-align: right;
  }
  .holder__name {
    font-family: "Fredoka", sans-serif; font-weight: 600;
    font-size: 22px; letter-spacing: 1.5px; color: var(--gold);
    white-space: nowrap;
  }
  .holder__cell {
    font-family: "Lato", sans-serif; font-size: 16px; color: var(--gold);
    margin-top: 2px;
  }
  .divider {
    position: absolute; left: 284px; top: 118px; width: 1px; height: 58px;
    background: rgba(242,242,238,0.35);
  }
  .contact {
    position: absolute; left: 306px; top: 140px;
    list-style: none;
    font-family: "Lato", sans-serif; font-size: 15px; color: var(--text-light);
  }
  .contact li { display: flex; align-items: center; gap: 6px; line-height: 22px; }
  .contact svg { width: 14px; height: 14px; fill: var(--gold); flex: none; }
  .address {
    position: absolute; left: 0; right: 0; top: 222px;
    text-align: center;
    font-family: "Lato", sans-serif; font-size: 16px; line-height: 22px; color: var(--text-light);
  }
</style>
</head>
<body>
<main class="canvas">
  <section class="card card--front" aria-label="Name card front">
    <div class="brand">
      <span class="brand__dot"></span>
      <span class="brand__name">BU-TIRAH</span>
    </div>
    <div class="card__band"></div>
  </section>

  <section class="card card--back" aria-label="Name card back">
    <div class="holder">
      <p class="holder__name">HAKIM RUSLAN</p>
      <p class="holder__cell">Cell : 86207319</p>
    </div>
    <div class="divider"></div>
    <ul class="contact">
      <li>
        <svg viewBox="0 0 16 16" aria-hidden="true"><path d="M2 5c0-2 2-3 6-3s6 1 6 3v1h-3V5H5v1H2z"/><path d="M4 7h8l2 6H2z"/></svg>
        64172859
      </li>
      <li>
        <svg viewBox="0 0 16 16" aria-hidden="true"><path d="M1 3h14v10H1z" /><path d="M1 3l7 6 7-6" fill="none" stroke="#043822" stroke-width="1.4"/></svg>
        rvk27@tealmail.com.sg
      </li>
    </ul>
    <p class="address">18 Pinegrove Industrial Road 2# 01-07<br>Singapore 748213</p>
    <div class="card__band"></div>
  </section>
</main>
</body>
</html>
```